Creative - Appealing - Business Card Design Project

Looking for a Business card design (vector artwork) for an existing company called 'Fernway Sound'. We operate in the entertainment industry specializing in audio system design and rental, however; we also deal with other sectors of the entertainment industry including lighting, video, staging and power system design and rental. We would like to see designs that don't focus too much on audio but include elements encompassing everything else.

Double sided business card, following our new colour scheme and logo, which is attached. The card would ideally be creative and eye catching to draw in new customers in the elegant event production market, such as weddings & corporate affairs.

Target Market(s)

High end corporate clients, wedding clients

Industry/Entity Type

Entertainment

Requirements
Must have
• Our contact details, these can be worded & listed however you think appropriate as part as the design

Business Name - Fernway Sound
My Name - Dominic Harwell
Web Address - www.fernwaysound-example.com
Mobile Number - 07914 362 517
Office Number - 0330 481 7265
Email - dom@fernwaysound-example.com

The name, email and mobile number would need to be able to be changed to my business partners also.

The font used on our logo is Sansation
Nice to have
• On one side maybe a word cloud involving the services in which we can provide; Lighting, Sound, Event Production, Staging, LED Uplighting, Projection Mapping, Wedding Hire

On the other side, all the important credentials of contact.
Should not have
• The design should not use any old style fonts (i.e Times New Roman, Gothic etc) or on the other side of the scale, any 'jokey' fonts (i.e. Comic Sans).

The font to be used is Sansation

```html
<!DOCTYPE html>
<html lang="en">
<head>
<meta charset="utf-8">
<title>Fernway Sound – Business Card</title>
<link rel="stylesheet" href="https://fonts.googleapis.com/css2?family=Alegreya+Sans:wght@400;500;700&family=Arimo&display=swap">
<style>
  :root {
    --backdrop: #9d8a7e;
    --card: #ffffff;
    --purple: #4e3481;
    --purple-deep: #2f1f57;
    --purple-light: #9a88c4;
    --grey: #707174;
    --grey-light: #c9c9cb;
    --ink: #141414;
    --label: #111111;
  }
  * { margin: 0; padding: 0; box-sizing: border-box; }
  html, body { width: 1200px; height: 1029px; overflow: hidden; }
  body {
    position: relative;
    background: var(--backdrop);
    font-family: "Alegreya Sans", sans-serif;
    color: var(--ink);
  }
  .card {
    position: absolute;
    width: 600px;
    height: 336px;
    background: var(--card);
    overflow: hidden;
    box-shadow: 6px 10px 18px rgba(0,0,0,0.35);
  }
  .card-front { left: 150px; top: 110px; }
  .card-back { left: 463px; top: 470px; }
  .card svg.swoosh { position: absolute; inset: 0; width: 100%; height: 100%; }

  .brand {
    position: absolute;
    left: 30px;
    top: 138px;
    display: flex;
    align-items: center;
    gap: 10px;
    color: var(--purple);
    font-weight: 700;
    font-size: 26px;
  }
  .brand-dot { width: 18px; height: 18px; border-radius: 50%; background: var(--purple); flex: none; }

  .divider {
    position: absolute;
    left: 238px;
    top: 40px;
    width: 2px;
    height: 200px;
    background: linear-gradient(var(--ink), var(--grey-light));
  }
  .contact { position: absolute; left: 256px; top: 38px; }
  .contact-name { color: var(--purple); font-size: 25px; font-weight: 500; line-height: 1.1; }
  .contact-company { font-size: 19px; margin-top: 2px; }
  .contact-list { list-style: none; margin-top: 14px; font-size: 16px; }
  .contact-list li { display: flex; align-items: center; gap: 8px; height: 24px; }
  .contact-list .icon { width: 14px; height: 14px; flex: none; }
  .contact-list .no-icon { width: 14px; }

  .back-mark {
    position: absolute;
    left: 230px;
    top: 20px;
    width: 140px;
    height: 140px;
    border-radius: 50%;
    background: linear-gradient(135deg, var(--purple-light), var(--purple-deep));
  }
  .back-name {
    position: absolute;
    left: 100px;
    top: 172px;
    color: var(--purple);
    font-size: 27px;
    letter-spacing: 7px;
  }
  .services { position: absolute; left: 118px; top: 222px; list-style: none; font-size: 19px; color: var(--ink); }
  .services li { height: 33px; display: flex; align-items: center; gap: 7px; }
  .services li::before {
    content: ""; width: 7px; height: 7px; border-radius: 50%; background: var(--purple);
  }

  .label { position: absolute; font-family: "Arimo", sans-serif; font-size: 24px; color: var(--label); }
  .label-front { left: 215px; top: 605px; }
  .label-back { left: 469px; top: 850px; }
</style>
</head>
<body>

<section class="card card-front" aria-label="Card front">
  <svg class="swoosh" viewBox="0 0 600 336" preserveAspectRatio="none" aria-hidden="true">
    <defs>
      <linearGradient id="front-purple" x1="0" x2="1" y1="0" y2="0">
        <stop offset="0" stop-color="#2f1f57"/>
        <stop offset="0.6" stop-color="#5a3f93"/>
        <stop offset="1" stop-color="#9a88c4"/>
      </linearGradient>
      <linearGradient id="front-grey" x1="0" x2="1">
        <stop offset="0" stop-color="#ffffff"/>
        <stop offset="1" stop-color="#bdbdbf"/>
      </linearGradient>
    </defs>
    <path d="M250 300 Q450 190 600 160 V336 H250 Z" fill="url(#front-grey)"/>
    <path d="M0 250 C80 250 150 268 230 310 L0 336 Z" fill="#0d0d0d"/>
    <path d="M0 296 C200 330 400 245 600 205 V336 H0 Z" fill="url(#front-purple)"/>
  </svg>

  <div class="brand"><span class="brand-dot"></span>Fernway Sound</div>
  <div class="divider"></div>

  <div class="contact">
    <p class="contact-name">Dominic Harwell</p>
    <p class="contact-company">Fernway Sound</p>
    <ul class="contact-list">
      <li><span class="no-icon"></span>07914 362 517</li>
      <li>
        <svg class="icon" viewBox="0 0 14 14" aria-hidden="true"><path d="M3 1 L5 1 L6 4 L4.5 5 Q5.5 8 9 9.5 L10 8 L13 9 L13 11 Q12 13 10 13 Q2 11 1 3 Q1 1 3 1 Z" fill="#555"/></svg>
        0330 481 7265
      </li>
      <li>
        <svg class="icon" viewBox="0 0 14 14" aria-hidden="true"><circle cx="7" cy="7" r="6" fill="none" stroke="#555" stroke-width="1.4"/><circle cx="7" cy="7" r="2.3" fill="none" stroke="#555" stroke-width="1.3"/></svg>
        dom@fernwaysound-example.com
      </li>
      <li>
        <svg class="icon" viewBox="0 0 14 14" aria-hidden="true"><circle cx="7" cy="7" r="6" fill="none" stroke="#555" stroke-width="1.3"/><ellipse cx="7" cy="7" rx="2.6" ry="6" fill="none" stroke="#555" stroke-width="1"/><path d="M1 7 H13 M2 4 H12 M2 10 H12" stroke="#555" stroke-width="1"/></svg>
        www.fernwaysound-example.com
      </li>
    </ul>
  </div>
</section>

<section class="card card-back" aria-label="Card back">
  <svg class="swoosh" viewBox="0 0 600 336" preserveAspectRatio="none" aria-hidden="true">
    <defs>
      <linearGradient id="back-purple" x1="0" x2="1">
        <stop offset="0" stop-color="#2f1f57"/>
        <stop offset="0.55" stop-color="#5a3f93"/>
        <stop offset="1" stop-color="#c6bbe0"/>
      </linearGradient>
    </defs>
    <path d="M0 180 C180 250 420 215 600 175 C420 205 180 225 0 205 Z" fill="url(#back-purple)"/>
    <path d="M0 205 C180 225 420 205 600 178 V336 H0 Z" fill="var(--grey)"/>
  </svg>

  <div class="back-mark" role="img" aria-label="Fernway Sound brand mark"></div>
  <p class="back-name">Fernway Sound</p>
  <ul class="services">
    <li>Lighting, Sound, Event Production</li>
    <li>Staging, LED Uplighting</li>
    <li>Projection Mapping, Wedding Hire</li>
  </ul>
</section>

<p class="label label-front">front</p>
<p class="label label-back">back</p>

</body>
</html>
```